Combining web page

We need a PSD webpage design for our PrestaShop store that shows food combining rules, you can see an example that we put here, you can follow the same information and food image combinations. You are just doing the design but the images when implemented on the website will be clickable that goes to product categories, all text and images will be editable.

This is just an example:
http://merrowtonic.com/content/7-food-combining-rules

Target Market(s)

Natural Product and supplement industry

Industry/Entity Type

Store

Number of Pages Required

1 page

Colors

Designer to choose colors to be used in the design.

Requirements
Must have
• 1. Clear images.
• 2. Clear readable text.
• 3. Company name shown Merrow Tonic.
• 4. Follow the food rules as seen on the web page example, but not the same design.
• 5. Logo should be seen.
• 7. All text and images will be editable.
• 8. Make sure the food images are in their proper groups.
• 9. You are not coping the design we gave you but the details have to be the same, copy the text and the image food groups are important, you cannot just put any food in a group, and the combinations are important.
Nice to have
• Here is the website it is for http://merrowtonic.com/

```html
<!DOCTYPE html>
<html lang="en">
<head>
<meta charset="utf-8">
<title>Food Combining Rules – Merrow Tonic</title>
<link href="https://fonts.googleapis.com/css2?family=Roboto+Slab:wght@400;500;700&family=Lobster&display=swap" rel="stylesheet">
<style>
  :root{
    --page:#ebebea;
    --board-edge:#d9d1c4;
    --ink:#2d2d2d;
    --muted:#8c8c8c;
    --label:#9a9a9a;
    --green:#6aa22a;
    --olive:#a88a2b;
    --brown:#b5561c;
    --red:#b3261e;
    --orange:#fbb017;
    --crimson:#a8231f;
    --white:#ffffff;
    --line:#e3e3e3;
  }
  *{box-sizing:border-box;margin:0;padding:0}
  html,body{width:1152px;height:1200px;overflow:hidden}
  body{background:var(--page);font-family:"Roboto Slab",serif;color:var(--ink);position:relative}
  .abs{position:absolute}

  .board{left:62px;top:40px;width:1040px;height:188px;background:linear-gradient(#f6f3ee,#ece6dc);border-radius:6px;box-shadow:0 6px 8px rgba(0,0,0,.18)}
  .board::after{content:"";position:absolute;left:0;right:0;bottom:0;height:10px;background:var(--board-edge);border-radius:0 0 6px 6px}
  .vine{top:0;width:110px;height:236px;border-radius:50px;background:linear-gradient(160deg,#7fb83a,#3f7d1c 60%,#a9d46a)}
  .vine.left{left:52px}
  .vine.right{right:52px}
  .tagline{left:0;width:1182px;top:50px;text-align:center;font-size:12.5px;letter-spacing:.06em;white-space:nowrap}
  .login{left:926px;top:50px;font-size:13px}
  .login svg{width:8px;height:8px;margin-left:3px}
  .search{left:177px;top:92px;width:208px;height:26px;border-bottom:1px solid #333;font-size:11px;font-style:italic;color:#555;padding-top:5px}
  .search svg{position:absolute;right:4px;top:1px;width:20px;height:20px}
  .brand{left:480px;width:200px;top:98px;display:flex;align-items:center;justify-content:center;gap:8px;font-size:22px;font-weight:700;color:var(--green);white-space:nowrap}
  .brand .mark{width:20px;height:20px;background:var(--red);flex:none}
  .cart{left:890px;top:95px;font-size:16px;color:var(--green);display:flex;align-items:center;gap:8px}
  .cart svg{width:22px;height:20px}
  .nav{left:270px;top:175px;display:flex;gap:36px;font-size:14px;letter-spacing:.04em}

  .card{left:108px;top:278px;width:936px;height:922px;background:var(--white)}
  .title{left:108px;width:936px;top:300px;text-align:center;font-family:"Lobster",cursive;font-size:30px;font-weight:400;color:#3a3a3a}
  .title em{font-style:normal;color:var(--green)}

  .band{left:108px;width:936px;height:160px}
  .band .num{position:absolute;left:0;top:0;width:84px;height:160px;color:#fff;font-weight:700;font-size:72px;display:flex;align-items:center;justify-content:center}
  .band .photo{position:absolute;left:84px;top:0;width:160px;height:160px;background:#fff;display:flex;align-items:center;justify-content:center}
  .band .photo div{width:116px;height:96px;border-radius:46%}
  .band .panel{position:absolute;left:244px;top:0;right:0;height:160px;color:#fff;padding:10px 16px}
  .band h2{font-size:14.5px;font-weight:700;padding-bottom:8px;border-bottom:1px solid rgba(255,255,255,.8);display:inline-block;width:129px;white-space:nowrap}
  .band .cols{display:flex;margin-top:10px;font-size:12px;line-height:16px;white-space:nowrap}
  .band .brand-r{position:absolute;right:18px;top:68px;display:flex;align-items:center;gap:8px;font-size:24px;font-weight:700;color:#fff;white-space:nowrap}
  .band .brand-r .mark{width:24px;height:24px;border-radius:50%;background:rgba(255,255,255,.9)}
  .b1{top:375px}.b1 .num,.b1 .panel{background:var(--orange)}
  .b2{top:970px}.b2 .num,.b2 .panel{background:var(--crimson)}

  .grid{left:108px;width:936px;display:grid;grid-template-columns:repeat(9,104px)}
  .cell{text-align:center;position:relative;padding-top:26px}
  .cell h3{font-size:11.2px;font-weight:500;color:var(--label);line-height:15px;height:48px}
  .cell.active{box-shadow:0 1px 6px rgba(0,0,0,.18);height:267px;background:#fff}
  .cell.active h3{color:#222}
  .food{width:76px;height:76px;margin:6px auto 0;border-radius:50%}
  .verdict{height:40px;margin-top:8px;display:flex;align-items:center;justify-content:center;gap:6px;color:var(--label)}
  .verdict svg{width:32px;height:32px}
  .notes{font-size:9.6px;line-height:13px;text-align:left;padding-left:22px;margin-top:4px;white-space:nowrap}
  .notes li{list-style:none;display:flex;align-items:center;gap:4px}
  .notes svg{width:9px;height:9px}
  .g-up{color:var(--green)}.g-fair{color:var(--olive)}.g-no{color:var(--brown)}.g-down{color:var(--red)}
  .row1{top:535px}
  .row2{top:1130px}

  .key{left:108px;width:936px;top:827px;height:45px;border-top:1px solid var(--line);border-bottom:1px solid var(--line);display:flex;align-items:center;padding-left:16px;font-size:14px;font-weight:500}
  .key strong{font-size:11px;color:#222;margin-right:48px}
  .key span{display:flex;align-items:center;gap:8px;margin-right:48px}
  .key svg{width:16px;height:16px}
  .note{left:124px;width:904px;top:881px;font-size:10.4px;line-height:15.2px;color:var(--muted)}
  .note strong{display:block;color:#222;font-size:11px;margin-bottom:3px}
</style>
</head>
<body>
<svg width="0" height="0" style="position:absolute">
  <defs>
    <symbol id="i-up" viewBox="0 0 24 24"><path d="M2 10h4v11H2z M8 21V10l4-8c1.5 0 2.5 1 2.5 2.5L14 9h6c1.2 0 2 1 1.8 2.2l-1.5 7.8c-.2 1.2-1.2 2-2.3 2z" fill="none" stroke="currentColor" stroke-width="2" stroke-linejoin="round"/></symbol>
    <symbol id="i-down" viewBox="0 0 24 24"><g transform="rotate(180 12 12)"><path d="M2 10h4v11H2z M8 21V10l4-8c1.5 0 2.5 1 2.5 2.5L14 9h6c1.2 0 2 1 1.8 2.2l-1.5 7.8c-.2 1.2-1.2 2-2.3 2z" fill="none" stroke="currentColor" stroke-width="2" stroke-linejoin="round"/></g></symbol>
    <symbol id="i-fair" viewBox="0 0 24 24"><g fill="none" stroke="currentColor" stroke-width="1.6" stroke-linejoin="round"><path d="M12 3v18M7 21h10M4 6h16M4 6l-3 7h6zM20 6l-3 7h6z"/><path d="M1 13a3 2 0 0 0 6 0M17 13a3 2 0 0 0 6 0"/></g></symbol>
    <symbol id="i-no" viewBox="0 0 24 24"><g fill="none" stroke="currentColor" stroke-width="3"><circle cx="12" cy="12" r="9.5"/><path d="M18.7 5.3 5.3 18.7"/></g></symbol>
  </defs>
</svg>

<div class="abs board"></div>
<div class="abs vine left" role="img" aria-label="Climbing ivy leaves along the left edge of the header"></div>
<div class="abs vine right" role="img" aria-label="Climbing ivy leaves along the right edge of the header"></div>
<p class="abs tagline">PURE TONICS FOR MODERN LIVING</p>
<p class="abs login">Login<svg viewBox="0 0 10 10"><path d="M1 3l4 4 4-4" fill="none" stroke="#333" stroke-width="1.5"/></svg></p>
<div class="abs search">Search<svg viewBox="0 0 24 24"><circle cx="10" cy="10" r="7.5" fill="none" stroke="#333" stroke-width="1.5"/><path d="M15.5 15.5 22 22" stroke="#333" stroke-width="1.5"/></svg></div>
<div class="abs brand"><span class="mark"></span>Merrow Tonic</div>
<div class="abs cart"><svg viewBox="0 0 24 22"><path d="M2 8h20l-2 12H4z M7 8l5-6 5 6 M8 11v6M12 11v6M16 11v6" fill="none" stroke="#444" stroke-width="1.5" stroke-linejoin="round"/></svg>(0 Cart)</div>
<nav class="abs nav"><span>OUR PRODUCTS</span><span>INGREDIENTS</span><span>HEALTH CONCERNS</span><span>OUR BLOGS</span><span>MORE</span></nav>

<div class="abs card"></div>
<h1 class="abs title">Food <em>Combining</em> Rules</h1>

<section class="abs band b1">
  <div class="num">1</div>
  <div class="photo"><div role="img" aria-label="Citrus fruits: limes, lemons, oranges and grapefruit halves" style="background:radial-gradient(circle at 40% 45%,#f6c336,#f28a1d 55%,#9dc93e)"></div></div>
  <div class="panel">
    <h2>CITRUS-ACID FRUITS</h2>
    <div class="cols">
      <div style="width:133px">Acerola cherry<br>Cranberry<br>Currants (red)<br>Grapefruit</div>
      <div style="width:101px">Kumquat<br>Lemon<br>Lime<br>Oranges</div>
      <div>Pomegranate<br>Tangelo<br>Tangerine</div>
    </div>
    <div class="brand-r"><span class="mark"></span>Merrow Tonic</div>
  </div>
</section>

<div class="abs grid row1">
  <div class="cell"><h3>Citrus-Acid<br>Fruits</h3><div class="food" role="img" aria-label="Citrus fruits" style="background:radial-gradient(#f7c431,#f08a24 60%,#a3c63f)"></div><div class="verdict g-up"><svg><use href="#i-up"/></svg></div></div>
  <div class="cell"><h3>Fruits<br>(sub-acid)</h3><div class="food" role="img" aria-label="Apple, pear, strawberry and blackberries" style="background:radial-gradient(#e6452f,#c9302a 50%,#2e2a35)"></div><div class="verdict g-up"><svg><use href="#i-up"/></svg></div></div>
  <div class="cell active"><h3>Sweet Fruits-<br>Palm Fruits</h3><div class="food" role="img" aria-label="Pineapple, bananas, coconut and dates" style="background:radial-gradient(#f4d35a,#c99a3a 55%,#5b3b24)"></div><div class="verdict g-fair"><svg><use href="#i-fair"/></svg></div>
    <ul class="notes g-up"><li><svg><use href="#i-up"/></svg>Pineapple</li><li><svg><use href="#i-up"/></svg>Coconut</li><li><svg><use href="#i-up"/></svg>Prunes</li></ul></div>
  <div class="cell"><h3>Neutral Fruits-<br>Raw Nuts-<br>Seeds</h3><div class="food" role="img" aria-label="Sunflower, avocado and mixed nuts" style="background:radial-gradient(#f2bf2a,#9b6a3a 55%,#6d8a2a)"></div><div class="verdict g-up"><svg><use href="#i-up"/></svg></div></div>
  <div class="cell"><h3>Grains</h3><div class="food" role="img" aria-label="Wheat ears and grains" style="background:radial-gradient(#e2c080,#c69650 60%,#a87a3e)"></div><div class="verdict g-no"><svg><use href="#i-no"/></svg></div>
    <ul class="notes g-fair"><li><svg><use href="#i-fair"/></svg>Pomegranate</li><li><svg><use href="#i-fair"/></svg>Cranberry</li></ul></div>
  <div class="cell"><h3>Legumes-<br>Sprouts</h3><div class="food" role="img" aria-label="Bean sprouts, green beans and peanuts" style="background:radial-gradient(#f0ecd8,#4e8f2a 60%,#c9a46a)"></div><div class="verdict"><svg class="g-fair"><use href="#i-fair"/></svg>-<svg class="g-no" style="width:28px;height:28px"><use href="#i-no"/></svg></div>
    <ul class="notes g-up"><li><svg><use href="#i-up"/></svg>Cranberries</li></ul></div>
  <div class="cell"><h3>Melons</h3><div class="food" role="img" aria-label="Watermelon, cantaloupe and honeydew" style="background:radial-gradient(#3b6e2a,#9cc257 55%,#f2a860)"></div><div class="verdict g-fair"><svg><use href="#i-fair"/></svg></div></div>
  <div class="cell"><h3>Succulent<br>Foods-<br>Tomatoes</h3><div class="food" role="img" aria-label="Corn, eggplant, cucumber and tomatoes" style="background:radial-gradient(#3a2a45,#e2c24a 50%,#d0261e)"></div><div class="verdict g-down"><svg><use href="#i-down"/></svg></div>
    <ul class="notes g-fair" style="padding-left:28px"><li><svg><use href="#i-fair"/></svg>Lemon</li></ul></div>
  <div class="cell"><h3>Vegetables<br>(leafy, Flower,<br>Root)</h3><div class="food" role="img" aria-label="Cabbage, potatoes, carrots and leafy greens" style="background:radial-gradient(#4f8a2c,#c9a04a 55%,#e2782a)"></div><div class="verdict g-down"><svg><use href="#i-down"/></svg></div>
    <ul class="notes g-fair" style="padding-left:28px"><li><svg><use href="#i-fair"/></svg>Lemon</li></ul></div>
</div>

<div class="abs key">
  <strong>Key:</strong>
  <span class="g-up"><svg><use href="#i-up"/></svg>Combines Well</span>
  <span class="g-fair"><svg><use href="#i-fair"/></svg>Fair Compatibility</span>
  <span class="g-no"><svg><use href="#i-no"/></svg>Not Recommended</span>
  <span class="g-down"><svg><use href="#i-down"/></svg>Not Compatible</span>
</div>
<div class="abs note"><strong>Note:</strong>Citrus fruits contain the highest levels of citric acid, as well as ascorbic acid and vitamin C. These fruits have a sharp flavor and can be tart. Citrus fruits include grapefruit, oranges, lemons, limes, tangelos, clementines, kumquat, and ugli fruit. Of all citrus fruits, lemons and limes contain the most citric acid, with about 4 grams of 100 grams of fruit.</div>

<section class="abs band b2">
  <div class="num">2</div>
  <div class="photo"><div role="img" aria-label="Sub-acid fruits: apple, pear, peach, strawberry and blackberries" style="background:radial-gradient(circle at 45% 45%,#e8553a,#d0322b 50%,#2d2a33 80%,#c7c24a)"></div></div>
  <div class="panel">
    <h2>FRUITS (SUB-ACID)</h2>
    <div class="cols">
      <div style="width:97px">Apples<br>Apricot<br>Banana<br>Cherries<br>Figs (fresh)<br>Guava</div>
      <div style="width:89px">Kiwi<br>Mangoes<br>Nectarine<br>Papaya<br>Peaches</div>
      <div style="width:105px">Pears<br>Persimmons<br>Pineapple<br>Plums<br>Prickly pear</div>
      <div style="width:109px">VINE &amp; BUSH<br>Blackberry<br>Blueberry<br>Boysenberry<br>Elderberry<br>Gooseberry</div>
      <div>Grapes (var.)<br>Huckleberry<br>Mulberry<br>Raspberries<br>Strawberries</div>
    </div>
    <div class="brand-r" style="right:14px"><span class="mark"></span>Merrow Tonic</div>
  </div>
</section>

<div class="abs grid row2">
  <div class="cell"><h3>Citrus-Acid<br>Fruits</h3></div>
  <div class="cell"><h3>Fruits<br>(sub-acid)</h3></div>
  <div class="cell"><h3>Sweet Fruits-<br>Palm Fruits</h3></div>
  <div class="cell"><h3>Neutral Fruits-<br>Raw Nuts-<br>Seeds</h3></div>
  <div class="cell"><h3>Grains</h3></div>
  <div class="cell"><h3>Legumes-<br>Sprouts</h3></div>
  <div class="cell"><h3>Melons</h3></div>
  <div class="cell"><h3>Succulent<br>Foods-<br>Tomatoes</h3></div>
  <div class="cell"><h3>Vegetables<br>(leafy, Flower,<br>Root)</h3></div>
</div>
</body>
</html>
```